Invitation for Executives

We need an eye-catching design for a direct mail invitation to executives. The invitation will be printed on A3 paper, so the image needs to be very crisp. The invitation details are attached in a word document. Note that the location details etc will be finalised at the end of the contest, so the winner will need to update the final file

Calloway Foundation has a special red colour that it uses for all marketing materials - the colour description is Pantone 1807 CMYK C:0 M:91 Y:94 K:30 RGB R:177 G:44 B:27 . Go to the website listed on the invitation details to have a look at the Calloway styles used on the website.
The Calloway logo is CALLOWAY in truesdell font, in the special red colour (or white if that red is the background)
Updates

Note - we have decided not to feature the Calloway logo - it will be enough to have the sponsorship byline and link to website, and let the speaker's credentials speak for themselves

Target Market(s)

senior executives (CEO's, CIOs, CFOs ) of major corporates and government agencies. These are busy people, but they are attracted by the idea of networking and mingling with their peers, as well as by the idea of hearing about a world they don't see too often (war zones) Usually they are 50+ years old, and are mostly men (but some women. They usually have pressing problems with the people around them, and want to help develop their teams.

Industry/Entity Type

Marketing

Requirements
Must have
• 1 page only
Nice to have
• something thought provoking or eye catching
Should not have
• any images with references to religion or violence

```html
<!DOCTYPE html>
<html lang="en">
<head>
<meta charset="utf-8">
<title>Executive Invitation – Conflict</title>
<link href="https://fonts.googleapis.com/css2?family=Orbitron:wght@900&family=Questrial&family=Open+Sans:ital,wght@0,700;1,300&family=Dancing+Script:wght@600&display=swap" rel="stylesheet">
<style>
  :root{
    --brand-red:#b12c1b;
    --paper:#ffffff;
    --backdrop:#000000;
    --ink:#1a1a1a;
    --soft-pink:#f2d4cf;
  }
  html,body{margin:0;padding:0;width:1200px;height:1200px;overflow:hidden;background:var(--backdrop);}
  .invitation{
    position:absolute;left:194px;top:66px;width:776px;height:1090px;
    background:var(--paper);overflow:hidden;
  }
  .header-band{position:absolute;left:0;top:0;width:100%;height:157px;background:var(--brand-red);}
  .headline{
    position:absolute;margin:0;white-space:nowrap;
    font-family:"Orbitron",sans-serif;font-weight:900;font-size:32px;letter-spacing:2.6px;line-height:1;
  }
  .headline--board{left:18px;top:57px;color:var(--paper);}
  .headline--home{left:112px;top:114px;color:var(--paper);}
  .headline--team{left:185px;top:163px;color:var(--brand-red);}
  .photo{position:absolute;left:0;top:0;}
  .intro{
    position:absolute;left:19px;top:232px;width:535px;margin:0;
    font-family:"Questrial",sans-serif;font-size:16.5px;line-height:22px;color:var(--ink);
  }
  .intro p{margin:0 0 21px;}
  .details-band{position:absolute;left:0;top:726px;width:100%;height:364px;background:var(--brand-red);border-top:4px solid var(--paper);}
  .detail{
    position:absolute;left:47px;margin:0;display:flex;
    font-family:"Open Sans",sans-serif;font-weight:700;font-size:14.5px;line-height:13px;color:var(--paper);
  }
  .detail-label{width:69px;}
  .detail--when{top:746px;}
  .detail--where{top:793px;}
  .detail--price{top:845px;}
  .bio{
    position:absolute;left:47px;top:904px;width:690px;margin:0;
    font-family:"Open Sans",sans-serif;font-style:italic;font-weight:300;font-size:15px;line-height:17.4px;color:var(--soft-pink);
  }
  .sponsor-script{
    position:absolute;left:484px;top:996px;margin:0;transform:rotate(-10deg);
    font-family:"Dancing Script",cursive;font-weight:600;font-size:19px;color:var(--paper);
  }
  .sponsor-name{
    position:absolute;right:46px;top:1020px;margin:0;
    font-family:"Open Sans",sans-serif;font-weight:700;font-size:27px;letter-spacing:1px;color:var(--paper);line-height:1;
  }
  .sponsor-line{
    position:absolute;right:46px;top:1050px;margin:0;
    font-family:"Questrial",sans-serif;font-size:13px;color:var(--paper);white-space:nowrap;
  }
</style>
</head>
<body>
<main class="invitation">
  <div class="header-band"></div>
  <h1 class="headline headline--board">CONFLICT WITH THE BOARD?</h1>
  <h1 class="headline headline--home">CONFLICT AT HOME?</h1>
  <h1 class="headline headline--team">CONFLICT IN YOUR TEAM?</h1>

  <svg class="photo" width="776" height="730" viewBox="0 0 776 730" role="img" aria-label="Photo of three business executives in suits gathered around a laptop at an office desk">
    <defs>
      <linearGradient id="photoTone" x1="0" y1="0" x2="1" y2="1">
        <stop offset="0" stop-color="#8a7566"/>
        <stop offset="0.55" stop-color="#5a4e48"/>
        <stop offset="1" stop-color="#c9a883"/>
      </linearGradient>
    </defs>
    <path d="M560 200 H776 V722 H220 V505 H275 V405 H560 Z" fill="url(#photoTone)"/>
  </svg>

  <div class="intro">
    <p>Conflict reduces effectiveness, creates political risk and can destroy relationships.&nbsp; For inspiration on helping those around you manage conflict, come along to hear <em>Dr. Miles Harlan</em>, entrepreneur, academic and “intercultural peacebuilder”. Miles has led conflict resolution projects around the world, from boardrooms and government agencies to Middle Eastern and Irish war zones.</p>
    <p>Join your peers for a fascinating<br>insight into serious conflict and<br>ways to build bridges<br>that endure.</p>
  </div>

  <div class="details-band"></div>
  <div class="detail detail--when"><span class="detail-label">WHEN:</span><span>Friday 13th August<br>3:00pm Start<br>4:30pm Networking and Nibbles</span></div>
  <div class="detail detail--where"><span class="detail-label">WHERE:</span><span>The Harbourview Room, 48 Marlow Street</span></div>
  <div class="detail detail--price"><span class="detail-label">PRICE:</span><span>Entry $15; RSVP 04 555 0123</span></div>

  <p class="bio">Dr. Harlan is Assistant Professor at Pacific Crest University, and was CEO of a successful internet startup sold to SportsWave in 2001. Currently, Dr. Harlan is working on a project in the Middle East with the Calloway Foundation and Common Ground Sports International to create sustainable peace among communities in Israel and the West Bank.</p>

  <p class="sponsor-script">Sponsored by</p>
  <p class="sponsor-name">CALLOWAY</p>
  <p class="sponsor-line">Sponsored by Calloway Oceania&nbsp; www.calloway.org</p>
</main>
</body>
</html>
```